Public Speaking Book for aspiring, ambitious speakers

I'm looking for a 6x9 book cover (Parcelo standard) as well as ebook and audiobook formats.

I'm looking for orange font on a white background as these are my brand colours.

Feel free to use some yellow and gold too if you deem it appropriate.

Title: Climb and Glow
Subtitle: Find Your Voice. Tell Your Story. Share your Message.
Author: Lionel Barstow

I would like to have a picture of a female speaker on the front cover.

Alternatively, some kind of image that symbolises public speaking like a microphone, podium etc

Target Market(s)

Aspiring professional speakers

Colors
f78f20

Requirements
Must have
• Correct spelling!
Nice to have
• A logo or picture that fits the theme, but no pressure if you can't think of anything
Should not have
• No men in suits please. I don't want this to have a 1980s corporate look.

```html
<!DOCTYPE html>
<html lang="en">
<head>
<meta charset="utf-8">
<title>Climb and Glow — Cover</title>
<link rel="stylesheet" href="https://fonts.googleapis.com/css2?family=Lato:wght@400;700&family=Caveat:wght@500&display=swap">
<style>
  :root {
    --stage: #c9d0d2;
    --sky-top: #c4dcee;
    --sky-bottom: #eaf3fb;
    --brand-orange: #f78f20;
    --ink: #1c1c1c;
    --photo-blue: #d3e4f2;
    --photo-orange: #f0733a;
  }
  * { box-sizing: border-box; margin: 0; padding: 0; }
  html, body {
    width: 1200px;
    height: 989px;
    overflow: hidden;
    background: var(--stage);
  }
  .canvas {
    position: relative;
    width: 1200px;
    height: 989px;
  }
  .cover {
    position: absolute;
    left: 300px;
    top: 45px;
    width: 600px;
    height: 900px;
    overflow: hidden;
    background: linear-gradient(160deg, var(--sky-top) 0%, #d8e8f5 45%, var(--sky-bottom) 100%);
    box-shadow: 0 12px 40px rgba(0,0,0,0.18);
  }
  .title {
    position: absolute;
    left: 0;
    right: 0;
    top: 70px;
    text-align: center;
    font-family: 'Lato', sans-serif;
    font-weight: 400;
    color: var(--brand-orange);
    line-height: 1;
  }
  .title-main {
    display: block;
    font-size: 190px;
    letter-spacing: -6px;
    line-height: 0.9;
  }
  .title-join {
    display: block;
    font-size: 58px;
    line-height: 0.7;
    margin-top: 4px;
  }
  .title-end {
    display: block;
    font-size: 168px;
    letter-spacing: -4px;
    line-height: 0.9;
  }
  .speaker-photo {
    position: absolute;
    left: 30px;
    top: 460px;
    width: 260px;
    height: 440px;
    background: linear-gradient(180deg, var(--photo-blue) 0%, #e3dde6 35%, #f2a47a 60%, var(--photo-orange) 100%);
  }
  .subtitle {
    position: absolute;
    right: 48px;
    top: 462px;
    text-align: right;
    color: var(--ink);
    font-family: 'Lato', sans-serif;
    font-size: 34px;
    line-height: 1.2;
    letter-spacing: -1px;
  }
  .subtitle-script {
    display: block;
    font-family: 'Caveat', cursive;
    font-weight: 500;
    font-size: 46px;
    line-height: 1.05;
    letter-spacing: 0;
    margin-top: 6px;
  }
  .author {
    position: absolute;
    right: 52px;
    bottom: 78px;
    font-family: 'Lato', sans-serif;
    font-size: 36px;
    color: var(--ink);
    letter-spacing: -0.5px;
  }
</style>
</head>
<body>
<main class="canvas">
  <section class="cover">
    <h1 class="title">
      <span class="title-main">Climb</span>
      <span class="title-join">and</span>
      <span class="title-end">Glow</span>
    </h1>

    <div class="speaker-photo" role="img" aria-label="Photo of a woman in an orange top speaking through a white megaphone, her other arm stretched out to the side"></div>

    <p class="subtitle">
      Find Your Voice.<br>
      Tell Your Story.
      <span class="subtitle-script">Share your<br>Message.</span>
    </p>

    <p class="author">Lionel Barstow</p>
  </section>
</main>
</body>
</html>
```